Tidewell Pronto Clinic Business card

We want a business card that matches our business theme. Our website is www.prontoclinicbz.example
The company name is Tidewell Pronto Clinic
The persons having the business cards will be doctors
My logo is attached.
We have a drive-thru medical center where our motto is Fast, Reliable, and Convenient. Our goal is to change the medical space while utilizing technologies, keeping a professional and clean look

Medical

Info on the card should be: Name, Position, Cell number, website, email address, possibly the office line as well

• Logo
• Professional medical feel with our logo colors incorporated

```html
<!DOCTYPE html>
<html lang="en">
<head>
<meta charset="utf-8">
<title>Tidewell Pronto Clinic – Business Card</title>
<link rel="stylesheet" href="https://fonts.googleapis.com/css2?family=Open+Sans:wght@400;600;700&display=swap">
<style>
  :root {
    --backdrop: #d3d6d7;
    --paper: #f2f2f0;
    --brand-blue: #1c3f9e;
    --accent-blue: #2fa8e0;
    --ink-grey: #6b6b6b;
    --ink-dark: #1b1b1b;
  }
  * { box-sizing: border-box; margin: 0; padding: 0; }
  html, body {
    width: 1200px; height: 1051px; overflow: hidden;
    background: var(--backdrop);
    font-family: "Open Sans", Arial, sans-serif;
  }
  .sheet {
    position: relative; width: 1200px; height: 1051px;
    display: flex; align-items: center; justify-content: center; gap: 50px;
  }
  .card {
    width: 520px; height: 300px;
    background: var(--paper);
    border-bottom: 4px solid var(--brand-blue);
    box-shadow: 0 10px 30px rgba(0,0,0,0.18);
    position: relative;
  }

  /* contact side */
  .card--contact .identity {
    position: absolute; right: 300px; top: 118px; text-align: right;
  }
  .identity .name {
    color: var(--brand-blue); font-weight: 700; font-size: 20px;
    letter-spacing: 0.3px; white-space: nowrap;
  }
  .identity .role {
    color: var(--ink-grey); font-size: 13px; margin-top: 2px;
  }
  .card--contact .divider {
    position: absolute; left: 236px; top: 118px;
    width: 1.5px; height: 86px; background: var(--brand-blue);
  }
  .contact-list {
    position: absolute; left: 252px; top: 120px; list-style: none;
  }
  .contact-list li {
    display: flex; align-items: center; gap: 8px;
    color: var(--ink-grey); font-size: 12.5px; line-height: 20px; white-space: nowrap;
  }
  .contact-list svg { width: 12px; height: 12px; flex: none; }

  /* brand side */
  .card--brand .wordmark {
    position: absolute; left: 0; right: 0; top: 112px;
    display: flex; align-items: center; justify-content: center; gap: 12px;
  }
  .wordmark .dot {
    width: 34px; height: 34px; border-radius: 50%; background: var(--brand-blue);
  }
  .wordmark .brand-name {
    color: var(--brand-blue); font-weight: 700; font-size: 26px; white-space: nowrap;
  }
  .card--brand .motto {
    position: absolute; left: 0; right: 0; top: 164px; text-align: center;
    color: var(--ink-dark); font-size: 12px; letter-spacing: 1px;
  }
</style>
</head>
<body>
<main class="sheet">
  <section class="card card--contact">
    <div class="identity">
      <p class="name">DARREN HOLLOWAY</p>
      <p class="role">President</p>
    </div>
    <div class="divider"></div>
    <ul class="contact-list">
      <li>
        <svg viewBox="0 0 12 12"><rect x="3" y="0.5" width="6" height="11" rx="1" fill="none" stroke="var(--accent-blue)" stroke-width="1.2"/><circle cx="6" cy="9.7" r="0.7" fill="var(--accent-blue)"/></svg>
        1300 555 014
      </li>
      <li>
        <svg viewBox="0 0 12 12"><path d="M2.5 1 L4.5 1 L5.3 3.6 L4 4.6 Q5.2 7 7.4 8 L8.4 6.7 L11 7.5 L11 9.5 Q10.5 11 9 11 Q3.5 10 1 3 Q1 1.5 2.5 1Z" fill="var(--accent-blue)"/></svg>
        1300 555 014
      </li>
      <li>
        <svg viewBox="0 0 12 12"><rect x="0.5" y="2.5" width="11" height="7.5" fill="var(--accent-blue)"/><path d="M0.5 2.5 L6 7 L11.5 2.5" fill="none" stroke="#fff" stroke-width="1"/></svg>
        darren@prontoclinicbz.example
      </li>
      <li>
        <svg viewBox="0 0 12 12"><circle cx="6" cy="6" r="5.3" fill="var(--accent-blue)"/><path d="M0.7 6 H11.3 M6 0.7 Q3 6 6 11.3 M6 0.7 Q9 6 6 11.3" fill="none" stroke="#fff" stroke-width="0.8"/></svg>
        www.prontoclinicbz.example
      </li>
    </ul>
  </section>

  <section class="card card--brand">
    <div class="wordmark">
      <span class="dot"></span>
      <span class="brand-name">Tidewell Pronto Clinic</span>
    </div>
    <p class="motto">FAST | RELIABLE | CONVENIENT</p>
  </section>
</main>
</body>
</html>
```